Company Website for an IT business called "BRIGHT HARBOR"

Complete website creation with text and graphics.
We need :
- modern and creative design for our IT company
- Content management system to edit text later on
- Integrate third party content from partner company
- Contact form (transfer by email)
Updates

Target Market(s)

Small and medium business
private customers

Industry/Entity Type

Information Technology

Coding

Coded - Design and coding required

Number of Pages Required

1 page

Font styles to use
Sans Serif

Requirements
Must have
• Contact form
Link to legal information
Link to data protection (GDPR)
Link to website owner declaration
Nice to have
• Fresh and creative graphics for IT business

```html
<!DOCTYPE html>
<html lang="en">
<head>
<meta charset="utf-8">
<title>Bright Harbor — IT Consultation &amp; Data Protection</title>
<link href="https://fonts.googleapis.com/css2?family=Ubuntu:wght@300;400;500&family=Montserrat:wght@300;400;500&family=Poppins:wght@400;600&display=swap" rel="stylesheet">
<style>
:root{
  --paper:#f4f4f4;
  --white:#ffffff;
  --navy:#0a4d8c;
  --ocean:#055a7c;
  --sky:#0aa0dd;
  --lavender:#efeef6;
  --ink:#2b2b2b;
  --grey:#7a7a7a;
  --heading-blue:#1f5b8c;
}
*{box-sizing:border-box;margin:0;padding:0}
html,body{width:1200px;height:4002px;overflow:hidden}
body{position:relative;background:var(--white);font-family:'Montserrat',sans-serif;color:var(--ink)}
.abs{position:absolute}
.band{position:absolute;left:0;width:1200px}

/* header */
.brand{left:134px;top:28px;font-family:'Ubuntu',sans-serif;font-weight:500;font-size:22px;color:var(--sky);letter-spacing:1px}
.nav{right:52px;top:36px;display:flex;gap:14px;font-family:'Ubuntu',sans-serif;font-size:12px;color:var(--navy);letter-spacing:.5px}

/* hero */
.hero-bg{top:0;height:660px;background:var(--paper)}
.hero-title{left:90px;top:288px;width:450px;text-align:center;font-family:'Ubuntu',sans-serif;font-weight:300;font-size:40px;line-height:49px;color:var(--heading-blue)}
.hero-blob{left:660px;top:130px;width:400px;height:400px}
.blob-name{left:660px;top:330px;width:400px;text-align:center;font-family:'Ubuntu',sans-serif;font-weight:500;font-size:26px;letter-spacing:2px;color:var(--white)}
.blob-tag{left:660px;top:380px;width:400px;text-align:center;font-family:'Montserrat',sans-serif;font-weight:300;font-size:19px;color:#cfe6f7}

/* intro */
.art{border-radius:50%}
.intro-art{left:151px;top:758px;width:346px;height:334px;border-radius:48% 48% 44% 44%;background:linear-gradient(160deg,#e7dcfb,#d7c8f5 60%,#c7d6f0)}
.intro-title{left:665px;top:800px;width:400px;font-family:'Ubuntu',sans-serif;font-weight:300;font-size:26px;line-height:37px;color:#1d3f5e}
.intro-copy{left:665px;top:892px;width:400px;font-size:12.4px;line-height:21px;color:var(--grey)}

/* solutions */
.solutions-bg{top:1380px;height:1700px;background:var(--ocean)}
.sol-title{left:0;top:1402px;width:1200px;text-align:center;font-family:'Ubuntu',sans-serif;font-weight:300;font-size:40px;color:var(--white)}
.sol-lead{left:260px;top:1472px;width:680px;text-align:center;font-family:'Ubuntu',sans-serif;font-size:15.5px;line-height:21px;color:var(--white)}
.service{width:456px;height:300px;border:1.5px solid #d9e7ef;border-radius:3px;text-align:center;color:var(--white)}
.service svg{display:block;margin:18px auto 0}
.service h3{font-family:'Ubuntu',sans-serif;font-weight:400;font-size:18px;margin-top:18px}
.service .rule{width:250px;height:2px;background:#d9e7ef;margin:38px auto 0}
.service p{font-family:'Ubuntu',sans-serif;font-size:14px;line-height:21px;margin:30px 20px 0}

/* promise cards */
.lavender-wave{top:2480px;height:600px}
.promise{width:357px;height:363px;background:var(--white);box-shadow:0 2px 10px rgba(0,0,0,.12);text-align:center}
.promise .art-box{width:154px;height:134px;margin:26px auto 0}
.promise h3{font-family:'Ubuntu',sans-serif;font-weight:400;font-size:19px;color:#1d3f5e;margin-top:26px}
.promise .rule{height:1px;background:#e6e6e6;margin:20px 14px 0}
.promise p{font-family:'Montserrat',sans-serif;font-weight:300;font-size:11.5px;line-height:19px;color:var(--grey);margin:28px 18px 0}

/* staff */
.staff-title{left:165px;top:2870px;font-family:'Ubuntu',sans-serif;font-size:27px;color:#1d3f5e}
.staff-copy{left:165px;top:2922px;width:400px;font-size:12.4px;line-height:21px;color:var(--grey)}
.staff-art{left:648px;top:2776px;width:400px;height:300px;border:6px solid #f3f3f8;border-radius:6px;background:linear-gradient(180deg,#3f4f96,#2c3470)}
.trend-bg{top:3065px;height:318px;background:var(--ocean)}
.trend{left:112px;top:3077px;width:974px;height:264px;background:var(--lavender);text-align:center}
.trend h2{font-family:'Ubuntu',sans-serif;font-weight:400;font-size:26px;color:#1d3f5e;margin-top:70px}
.trend p{font-size:12.4px;line-height:21px;color:var(--grey);margin:28px 48px 0}

/* contact */
.contact-bg{top:3383px;height:580px;background:var(--paper)}
.contact-title{left:126px;top:3535px;font-family:'Ubuntu',sans-serif;font-weight:400;font-size:56px;color:#173654}
.contact-copy{left:126px;top:3665px;width:480px;font-size:13.4px;line-height:21px;color:#444}
.contact-copy p+p{margin-top:21px}
.field{left:676px;width:390px;background:var(--white);border:1px solid #d5d5d5;border-radius:20px;padding:12px 13px;font-family:'Poppins',sans-serif;font-size:13px;color:#8a8a8a}
.send{left:676px;top:3764px;width:390px;height:41px;border-radius:21px;background:var(--sky);color:var(--white);font-family:'Poppins',sans-serif;font-weight:600;font-size:14px;text-align:center;line-height:41px}

/* footer */
.footer{top:3963px;height:39px;background:var(--ocean);color:var(--white);font-family:'Montserrat',sans-serif;font-size:12.5px;text-align:center;line-height:39px}
.footer span{padding:0 8px}
.footer span+span{border-left:1px solid #fff}
</style>
</head>
<body>

<!-- hero -->
<div class="band hero-bg"></div>
<svg class="band" style="top:620px" width="1200" height="60" viewBox="0 0 1200 60" preserveAspectRatio="none">
  <path d="M0 28 C300 12 500 6 800 14 S1100 30 1200 40 L1200 60 L0 60Z" fill="var(--white)"/>
</svg>
<div class="abs brand">BRIGHT HARBOR</div>
<nav class="abs nav"><span>HOME</span><span>ABOUT</span><span>SOLUTIONS</span><span>STAFF</span><span>CONTACT</span></nav>
<h1 class="abs hero-title">IT Consultation &amp; Data Protection</h1>
<svg class="abs hero-blob" viewBox="0 0 400 400">
  <path d="M150 40 C190 0 280 -5 330 50 C385 110 395 230 380 300 C360 380 220 400 150 380 C60 350 10 290 25 200 C35 120 95 110 150 40Z" fill="var(--sky)"/>
  <path d="M140 52 C180 15 270 10 318 60 C368 115 370 230 352 295 C330 365 210 385 140 365 C60 340 15 285 28 200 C40 125 95 110 140 52Z" fill="var(--navy)"/>
</svg>
<div class="abs blob-name">BRIGHT HARBOR</div>
<div class="abs blob-tag">Quality. Experience. Integrity.</div>

<!-- intro -->
<div class="abs intro-art" role="img" aria-label="Illustration of a team working together around a desk with gears and a light bulb"></div>
<h2 class="abs intro-title">We Make Customized Solutions For You</h2>
<p class="abs intro-copy">Lorem ipsum dolor sit amet, consectetur adipiscing elit, sed do eiusmod tempor incididunt ut labore et dolore magna aliqua. Ut enim ad minim veniam, quis nostrud exercitation ullamco laboris nisi ut aliquip ex ea commodo consequat. Duis aute irure dolor in reprehenderit in voluptate velit esse cillum dolore eu fugiat nulla pariatur. Excepteur sint occaecat cupidatat non proident, sunt in culpa qui officia deserunt mollit anim id est laborum</p>

<!-- solutions -->
<svg class="band" style="top:1280px" width="1200" height="130" viewBox="0 0 1200 130">
  <path d="M0 130 L0 70 C20 80 20 120 10 130 Z M0 130 L60 110 C90 90 130 95 140 110 C170 80 230 80 250 100 C280 70 320 70 330 90 C350 60 400 50 420 70 C430 30 480 20 500 40 C520 10 570 15 590 40 C620 30 650 50 660 70 C700 60 720 70 740 50 C760 10 820 10 840 40 C870 30 910 40 920 60 C960 50 1000 70 1020 80 C1060 70 1100 80 1120 90 C1150 60 1190 65 1200 75 L1200 130Z" fill="var(--ocean)"/>
</svg>
<div class="band solutions-bg"></div>
<h2 class="abs sol-title">Tailor-Made Solutions</h2>
<p class="abs sol-lead">You just need to know what you want to leave the rest to us. We offer IT solutions to your problem and to your satisfaction. Looking for a web developer? We have your back. Some of our services include:</p>

<div class="abs service" style="left:126px;top:1596px">
  <svg width="80" height="92" viewBox="0 0 80 92" fill="none" stroke="#fff" stroke-width="2.5"><rect x="6" y="4" width="40" height="84" rx="5"/><line x1="6" y1="16" x2="46" y2="16"/><line x1="6" y1="76" x2="46" y2="76"/><rect x="28" y="28" width="46" height="34" fill="var(--ocean)"/><line x1="46" y1="38" x2="68" y2="38"/><line x1="46" y1="46" x2="68" y2="46"/><line x1="46" y1="54" x2="62" y2="54"/><text x="32" y="52" fill="#fff" stroke="none" font-size="16" font-family="Ubuntu,sans-serif">$</text></svg>
  <h3>Accredited Fintech Applications</h3><div class="rule"></div>
  <p>Lorem ipsum dolor sit amet, consectetur adipiscing elit, sed do eiusmod tempor incididunt ut labore et dolore magna aliqua.</p>
</div>
<div class="abs service" style="left:617px;top:1596px">
  <svg width="92" height="92" viewBox="0 0 92 92" fill="none" stroke="#fff" stroke-width="2.5"><circle cx="46" cy="40" r="12"/><circle cx="46" cy="40" r="4"/><circle cx="16" cy="18" r="5"/><circle cx="16" cy="62" r="5"/><circle cx="76" cy="18" r="5"/><circle cx="76" cy="62" r="5"/><line x1="20" y1="21" x2="36" y2="33"/><line x1="20" y1="59" x2="36" y2="47"/><line x1="72" y1="21" x2="56" y2="33"/><line x1="72" y1="59" x2="56" y2="47"/><line x1="46" y1="52" x2="46" y2="86"/></svg>
  <h3>Let Artificial Intelligence do it for you.</h3><div class="rule"></div>
  <p>Lorem ipsum dolor sit amet, consectetur adipiscing elit, sed do eiusmod tempor incididunt ut labore et dolore magna aliqua.</p>
</div>
<div class="abs service" style="left:126px;top:1933px">
  <svg width="92" height="92" viewBox="0 0 92 92" fill="none" stroke="#fff" stroke-width="2.5"><circle cx="46" cy="42" r="26"/><circle cx="46" cy="42" r="12"/><g stroke-width="6"><line x1="46" y1="6" x2="46" y2="14"/><line x1="46" y1="70" x2="46" y2="78"/><line x1="10" y1="42" x2="18" y2="42"/><line x1="74" y1="42" x2="82" y2="42"/><line x1="20" y1="16" x2="26" y2="22"/><line x1="66" y1="62" x2="72" y2="68"/><line x1="72" y1="16" x2="66" y2="22"/><line x1="20" y1="68" x2="26" y2="62"/></g></svg>
  <h3>Create the Service-We Will Handle the Rest</h3><div class="rule"></div>
  <p>Lorem ipsum dolor sit amet, consectetur adipiscing elit, sed do eiusmod tempor incididunt ut labore et dolore magna aliqua.</p>
</div>
<div class="abs service" style="left:617px;top:1933px">
  <svg width="92" height="92" viewBox="0 0 92 92" fill="none" stroke="#fff" stroke-width="2.5"><circle cx="40" cy="40" r="30"/><circle cx="40" cy="40" r="23"/><polyline points="24,48 34,34 46,44 56,30"/><line x1="62" y1="62" x2="84" y2="84" stroke-width="7"/></svg>
  <h3>Do the Job-We will do the Analysis.</h3><div class="rule"></div>
  <p>Lorem ipsum dolor sit amet, consectetur adipiscing elit, sed do eiusmod tempor incididunt ut labore et dolore magna aliqua.</p>
</div>

<svg class="band lavender-wave" width="1200" height="600" viewBox="0 0 1200 600" preserveAspectRatio="none">
  <path d="M0 20 C300 40 500 70 700 70 C900 70 1100 40 1200 10 L1200 600 L0 600Z" fill="var(--lavender)"/>
</svg>
<div class="abs promise" style="left:219px;top:2315px">
  <div class="art-box" role="img" aria-label="Illustration of a secure login screen with a padlock and a guard" style="background:linear-gradient(135deg,#ebe8f8,#dcd8f3)"></div>
  <h3>Your Data Is Protected</h3><div class="rule"></div>
  <p>Lorem ipsum dolor sit amet, consectetur adipiscing elit, sed do eiusmod tempor incididunt ut labore et dolore magna aliqua.</p>
</div>
<div class="abs promise" style="left:598px;top:2315px">
  <div class="art-box" role="img" aria-label="Illustration of a hand ticking a customer satisfaction survey" style="background:linear-gradient(135deg,#ece6dd,#e2d9cd)"></div>
  <h3>Pay After Satisfaction</h3><div class="rule"></div>
  <p>Lorem ipsum dolor sit amet, consectetur adipiscing elit, sed do eiusmod tempor incididunt ut labore et dolore magna aliqua.</p>
</div>

<!-- staff -->
<h2 class="abs staff-title">Tech-Savvy Staff</h2>
<p class="abs staff-copy">Lorem ipsum dolor sit amet, consectetur adipiscing elit, sed do eiusmod tempor incididunt ut labore et dolore magna aliqua.</p>
<div class="band trend-bg"></div>
<div class="abs trend">
  <h2>We Set The Trend Or Catch It When It Happens.</h2>
  <p>Lorem ipsum dolor sit amet, consectetur adipiscing elit, sed do eiusmod tempor incididunt ut labore et dolore magna aliqua. Ut enim ad minim veniam, quis nostrud exercitation ullamco laboris nisi ut aliquip ex ea commodo consequat. Duis aute irure dolor in reprehenderit in voluptate velit esse cillum dolore eu fugiat nulla pariatur. Excepteur sint occaecat cupidatat non proident, sunt in culpa qui officia deserunt mollit anim id est laborum</p>
</div>
<div class="abs staff-art" role="img" aria-label="Illustration of three developers with laptops sitting on a large screen full of code"></div>

<!-- contact -->
<div class="band contact-bg"></div>
<h2 class="abs contact-title">Get In Touch</h2>
<div class="abs contact-copy">
  <p>Our team is always eager to hear from you. Whether you want to consult, get a quote or give feedback, we are here to listen and respond.</p>
  <p>Fill the form, and we will get<br>back to you.</p>
</div>
<div class="abs field" style="top:3521px;height:41px;padding-top:10px">Name</div>
<div class="abs field" style="top:3571px;height:41px;padding-top:10px">Your Email</div>
<div class="abs field" style="top:3621px;height:133px">Your Message</div>
<div class="abs send">Send Message</div>

<footer class="band footer"><span>Copyright © 2020 Bright Harbor</span><span>Bright Harbor is fully compliant with the GDPR guidelines.</span></footer>

</body>
</html>
```